そよかぜ日記(http://www.soyokaze-nikki.com/)から発刊した、Lumora電子書籍の表紙のデザインをコンペ形式で募集いたします。 電子書籍「庭仕事の始め方: 3年で畑を百坪に広げた家庭菜園術」(http://www.shoppomart.jp/exec/tenpo/item/Q77KTX3MZA/) の表紙をリニューアルします。 ファイル形式はjpeg(1600×2560px) 50MB未満でお願いします。 .psdファイルも一緒に納品してください(.pdfも可能)。 白地または非常に薄い背景色の表紙画像は、白い背景との区別がつかなくなる場合があります。幅の狭い (3 ~ 4 ピクセル) 薄灰色の枠線を追加して、表紙の境界を明確にしてください。 現在の表紙デザインに沿う必要はありません。書籍の魅力・内容をしっかりアピールしてくれるデザインを選んで採用させていただきます。 ご不明点や質問はお気軽にご相談ご相談ください。 たくさんのデザイナーの皆様からのご連絡・ご提案をお待ちしております。 |
タイトルが目につきやすいことと、シンプルですが軽くない感じのデザインが気に入りました。
皆さま、多くのご提案ありがとうございました。色々なタイプのデザインを拝見させていただくことができました。これから出版する電子書籍については、コンペで作ってもらおうと考えています。これからもよろしくお願いします。

```html
<!DOCTYPE html>
<html lang="ja">
<head>
<meta charset="utf-8">
<title>庭仕事の始め方</title>
<link href="https://fonts.googleapis.com/css2?family=Dela+Gothic+One&family=M+PLUS+1p:wght@700;800&display=swap" rel="stylesheet">
<style>
:root{
  --sky-deep:#1f86d6;
  --sky-light:#8fd2f7;
  --grid:rgba(255,255,255,.55);
  --curve:#e23fd8;
  --title-pink:#ea3a9c;
  --title-edge:#ffffff;
  --title-shadow:#1a3f7a;
  --band:#fff23a;
  --ink:#111111;
  --accent-red:#e0201b;
  --bubble:#ffffff;
  --frame:#d6d6d6;
}
*{margin:0;padding:0;box-sizing:border-box}
html,body{width:749px;height:1200px;overflow:hidden;background:#fff}
.cover{
  position:relative;width:749px;height:1200px;overflow:hidden;
  border:4px solid var(--frame);
  background:radial-gradient(ellipse at 55% 45%, var(--sky-light) 0%, #4fb0ea 45%, var(--sky-deep) 100%);
  font-family:"M PLUS 1p",sans-serif;
}
.chart{position:absolute;inset:0}
.keyword{font-family:"M PLUS 1p",sans-serif;font-weight:800;fill:var(--ink);text-anchor:middle;dominant-baseline:central}
.title{
  position:absolute;left:30px;top:62px;
  writing-mode:vertical-rl;
  font-family:"Dela Gothic One",sans-serif;
  font-weight:400;
  color:var(--title-pink);
  -webkit-text-stroke:10px var(--title-edge);
  paint-order:stroke fill;
  text-shadow:6px 6px 0 var(--title-shadow);
  transform:skewY(6deg);
  transform-origin:top left;
  line-height:1;
}
.title .big{font-size:108px;letter-spacing:4px}
.title .small{font-size:76px;margin:8px 0}
.band{
  position:absolute;left:0;right:0;top:898px;bottom:0;background:var(--band);
}
.band .lead{
  position:absolute;left:196px;top:28px;font-size:29px;font-weight:800;color:var(--ink);white-space:nowrap;
}
.band .subtitle{
  position:absolute;left:196px;top:76px;font-size:29px;font-weight:800;color:var(--accent-red);white-space:nowrap;
}
.brand{
  position:absolute;left:20px;top:122px;width:150px;height:150px;border-radius:50%;
  background:#ffffff;border:4px solid var(--ink);
  display:flex;align-items:center;justify-content:center;
  font-size:21px;font-weight:800;color:var(--ink);white-space:nowrap;
}
.band .url{
  position:absolute;right:26px;top:206px;font-size:21px;font-weight:700;color:var(--ink);white-space:nowrap;
}
</style>
</head>
<body>
<div class="cover">
  <svg class="chart" width="749" height="1200" viewBox="0 0 749 1200">
    <g stroke="var(--grid)" stroke-width="3">
      <line x1="0" y1="120" x2="749" y2="120"/>
      <line x1="0" y1="227" x2="749" y2="227"/>
      <line x1="0" y1="334" x2="749" y2="334"/>
      <line x1="0" y1="441" x2="749" y2="441"/>
      <line x1="0" y1="548" x2="749" y2="548"/>
      <line x1="0" y1="655" x2="749" y2="655"/>
      <line x1="0" y1="762" x2="749" y2="762"/>
    </g>
    <path d="M40 725 C220 720 360 700 470 640 C570 585 630 480 660 360 C675 300 688 250 699 200"
          fill="none" stroke="var(--curve)" stroke-width="8" stroke-linecap="round"/>
    <g fill="var(--curve)">
      <circle cx="40" cy="725" r="9"/><circle cx="110" cy="723" r="9"/><circle cx="180" cy="720" r="9"/>
      <circle cx="250" cy="714" r="9"/><circle cx="320" cy="705" r="9"/><circle cx="390" cy="688" r="9"/>
      <circle cx="455" cy="650" r="9"/><circle cx="515" cy="607" r="9"/><circle cx="565" cy="560" r="9"/>
      <circle cx="605" cy="500" r="9"/><circle cx="635" cy="435" r="9"/><circle cx="655" cy="370" r="9"/>
      <circle cx="670" cy="305" r="9"/><circle cx="685" cy="250" r="9"/><circle cx="699" cy="200" r="14"/>
    </g>
    <g fill="var(--bubble)">
      <ellipse cx="448" cy="200" rx="105" ry="38"/>
      <ellipse cx="280" cy="360" rx="78" ry="36"/>
      <ellipse cx="510" cy="368" rx="72" ry="30"/>
      <ellipse cx="420" cy="512" rx="72" ry="38"/>
      <ellipse cx="640" cy="552" rx="62" ry="48"/>
      <ellipse cx="275" cy="621" rx="72" ry="36"/>
      <ellipse cx="574" cy="707" rx="62" ry="42"/>
    </g>
    <text class="keyword" x="448" y="200" font-size="36">土作り</text>
    <text class="keyword" x="280" y="360" font-size="32">種まき</text>
    <text class="keyword" x="510" y="368" font-size="27">水やり</text>
    <text class="keyword" x="420" y="512" font-size="38">肥料</text>
    <text class="keyword" x="640" y="552" font-size="36">収穫</text>
    <text class="keyword" x="275" y="621" font-size="30">道具</text>
    <text class="keyword" x="574" y="707" font-size="38">野菜</text>
  </svg>

  <h1 class="title"><span class="big">庭仕事</span><span class="small">の</span><span class="big">始め方</span></h1>

  <div class="band">
    <p class="lead">そよかぜ日記を運営中ののぶ助による</p>
    <p class="subtitle">3年で畑を百坪に広げた家庭菜園術</p>
    <div class="brand">そよかぜ日記</div>
    <p class="url">http://www.soyokaze-nikki.com/</p>
  </div>
</div>
</body>
</html>
```